WordPress webdesign with coding for our company BRISK The Answer

BRISK The Answer is a payrolling company such as Alpenwage Staffing (one of our competitor https://www.alpenwage-staffing.example/fr/). We need to set up our website in both languages (Fr and Eng). Our logo is enclosed.
we would like something simple explaining what is payrolling in Graph and wording, who we are and a contact page. you can also take some example if needed from our mother company BRISK The Horizon (www.briskthehorizon.example) or our sister company (www.briskyourstride.example). we would like to keep the color panel of our logo (ref. Black = PANTONE P Process Black C
Pink = PANTONE P Process Magenta C
Grey = PANTONE 430 C) as the driver of the website.

```html
<!DOCTYPE html>
<html lang="en">
<head>
<meta charset="utf-8">
<title>BRISK The Answer – Payrolling</title>
<link rel="stylesheet" href="https://fonts.googleapis.com/css2?family=Poppins:ital,wght@0,400;0,500;0,600;0,700;0,800;1,400&display=swap">
<style>
:root{
  --magenta:#ec1a8c;
  --magenta-soft:#f7c7e0;
  --blush:#fdeef5;
  --ink:#2b2b2e;
  --text:#4d4d52;
  --grey:#f3f3f4;
  --grey-mid:#c9c9cc;
  --dark:#333438;
  --white:#fff;
}
*{box-sizing:border-box;margin:0;padding:0}
html,body{width:1200px;height:4104px;overflow:hidden}
body{position:relative;font-family:"Poppins",sans-serif;color:var(--text);background:var(--white)}
.abs{position:absolute}
.bg-wash{left:0;top:0;width:1200px;height:4104px;background:
  radial-gradient(circle at 0 0,#fde3f0 0,transparent 420px),
  radial-gradient(circle at 1200px 1300px,#fde3f0 0,transparent 380px),
  radial-gradient(circle at 0 2900px,#fde3f0 0,transparent 420px)}
/* header */
.brand{left:95px;top:22px;width:240px}
.brand-name{font-weight:700;font-size:44px;color:var(--ink);letter-spacing:2px;line-height:1}
.brand-tag{font-size:13px;letter-spacing:11px;color:var(--ink);margin-top:4px}
.nav{left:532px;top:38px;display:flex;gap:31px;font-size:13px;font-weight:500;color:var(--ink);text-transform:uppercase}
.nav .active{color:var(--magenta)}
.lang{left:988px;top:28px;width:128px;height:40px;border-radius:20px;background:#ececee;display:flex;align-items:center;justify-content:center;gap:8px;font-size:12px;font-weight:600;color:var(--ink)}
.lang-dot{width:20px;height:20px;border-radius:50%;background:linear-gradient(#3b4ea1 50%,#d8262e 50%)}
/* hero */
.hero-title{left:88px;top:252px;font-size:40px;font-weight:700;color:var(--ink);line-height:1.17}
.hero-text{left:88px;top:422px;width:390px;font-size:13px;line-height:1.8}
.btn{display:flex;align-items:center;justify-content:center;background:var(--magenta);color:var(--white);font-weight:600;font-size:12px;border-radius:30px;text-transform:uppercase}
.hero-btn{left:88px;top:513px;width:165px;height:48px}
.photo{background:linear-gradient(135deg,#d9dde2,#9aa0a8)}
.round{border-radius:50%}
.tablet{left:665px;top:231px;width:480px;height:367px;border-radius:18px;background:#1d1d1f;padding:14px}
.tablet .photo{width:100%;height:100%;border-radius:8px;background:linear-gradient(135deg,#e8e8ea,#8d9299)}
.ghost-word{left:-6px;top:640px;font-size:140px;font-weight:800;color:#f1f1f2;line-height:1}
/* trust */
.trust-panel{left:88px;top:794px;width:1023px;height:306px;border-radius:40px;background:var(--blush)}
.section-title{font-weight:700;color:var(--ink);text-align:center}
.trust-title{left:0;width:1200px;top:862px;font-size:18px;font-weight:600}
.card{background:var(--white);border-radius:10px;box-shadow:0 10px 30px rgba(0,0,0,.06);text-align:center;padding:28px 30px}
.card svg{display:block;margin:0 auto 14px}
.card h3{font-size:14px;font-weight:600;color:var(--ink);margin-bottom:10px}
.card p{font-size:12px;line-height:1.65}
/* payrolling */
.pay-photo{left:88px;top:1325px;width:558px;height:352px;border-radius:14px;border:2px solid var(--ink)}
.pay-title{left:705px;top:1382px;font-size:28px;font-weight:600;color:var(--ink)}
.pay-text{left:705px;top:1440px;width:355px;font-size:12px;line-height:1.95}
.bullets{left:705px;top:1570px;list-style:none;font-size:12px;font-weight:500;color:var(--ink)}
.bullets li{margin-bottom:10px;display:flex;align-items:center;gap:8px}
.bullets li::before{content:"";width:6px;height:6px;border-radius:50%;background:var(--magenta)}
.tagline{left:0;width:1200px;top:1735px;text-align:center;font-size:17px;font-weight:500;color:var(--ink)}
/* about */
.grey-band{left:0;top:2206px;width:1200px;height:416px;background:var(--grey)}
.about-label{left:179px;top:1956px;font-size:17px;color:var(--magenta)}
.about-title{left:179px;top:1992px;font-size:27px;font-weight:600;color:var(--ink)}
.about-text{left:179px;top:2050px;width:330px;font-size:12px;line-height:1.95}
.play{left:601px;top:2179px;width:96px;height:96px;border-radius:50%;background:var(--magenta);display:flex;align-items:center;justify-content:center}
/* mission */
.mission-title{left:0;width:1200px;top:2366px;font-size:27px}
.mcard{width:263px;height:246px;top:2440px;border-radius:14px;background:linear-gradient(160deg,#d6d4d2,#8a8784)}
.mlabel{top:2624px;width:215px;height:102px;border:1.5px solid var(--magenta);border-radius:12px;background:var(--white);display:flex;align-items:center;justify-content:center;text-align:center;font-size:12px;font-weight:600;color:var(--ink);line-height:1.6;padding:0 28px}
/* testimonial */
.test-title{left:0;width:1200px;top:2823px;font-size:27px}
.quote-box{left:551px;top:2887px;width:96px;height:96px;border-radius:16px;background:var(--magenta)}
.quote-ghost{left:170px;top:2920px}
.quote-text{left:230px;top:3008px;width:740px;text-align:center;font-style:italic;font-size:15px;line-height:1.7}
.stars{left:0;width:1200px;top:3100px;text-align:center;color:var(--magenta);font-size:22px;letter-spacing:4px}
.author{left:0;width:1200px;top:3136px;text-align:center;font-size:16px;font-weight:500;color:var(--ink)}
.dots{left:582px;top:3189px;display:flex;gap:4px}
.dots i{width:9px;height:9px;background:var(--magenta-soft)}
.dots i:first-child{background:var(--magenta)}
/* footer */
.footer-shape{left:0;top:3650px}
.form-card{left:231px;top:3292px;width:368px;height:430px;border-radius:40px;background:var(--magenta);padding:30px 36px}
.form-card h2{text-align:center;color:var(--white);font-size:29px;font-weight:600;margin-bottom:18px}
.field{height:35px;background:var(--white);border-radius:5px;margin-bottom:9px;font-size:11px;color:#555;padding:10px 16px}
.field.area{height:89px}
.send{left:352px;top:3657px;width:126px;height:37px;background:var(--dark)}
.talk-title{left:660px;top:3440px;font-size:40px;font-weight:700;color:var(--ink)}
.talk-text{left:662px;top:3517px;width:340px;font-size:12px;line-height:1.95}
.f-brand{left:124px;top:3838px}
.f-brand .brand-name{color:var(--white);font-size:58px}
.f-brand .brand-tag{color:var(--white);font-size:15px;letter-spacing:16px}
.fcol{color:var(--white);font-size:12px}
.fcol h4{font-size:15px;font-weight:600;margin-bottom:14px}
.fcol p{margin-bottom:10px;color:#e6e6e8}
.fcol .ic{color:var(--magenta);margin-right:8px}
.f-rule{left:88px;top:4049px;width:1024px;height:1px;background:#55565b}
.copy{left:0;width:1200px;top:4070px;text-align:center;font-size:11px;font-weight:600;color:var(--white)}
.to-top{left:1140px;top:4031px;width:40px;height:40px;border-radius:50%;background:var(--magenta);display:flex;align-items:center;justify-content:center}
</style>
</head>
<body>
<div class="abs bg-wash"></div>

<header>
  <div class="abs brand"><div class="brand-name">BRISK</div><div class="brand-tag">THE ANSWER</div></div>
  <nav class="abs nav"><span class="active">Home</span><span>What is payrolling</span><span>Who we are</span><span>Contact</span></nav>
  <div class="abs lang"><span class="lang-dot"></span>ENGLISH <span style="color:var(--magenta)">⌄</span></div>
</header>

<section class="hero">
  <h1 class="abs hero-title">Smart Payrolling<br>Solutions for a<br>Flexible Workforce</h1>
  <p class="abs hero-text">We simplify employment administration by taking care of payroll, compliance, and contracts — so you can focus on growing your business.</p>
  <div class="abs btn hero-btn">Get in touch</div>
  <svg class="abs" style="left:700px;top:100px" width="500" height="640" viewBox="0 0 500 640">
    <path d="M144 8 A180 180 0 0 1 324 188 L144 188Z" fill="#ec1a8c"/>
    <path d="M500 100 A120 120 0 0 0 500 340Z" fill="#f7a6cf"/>
    <path d="M500 230 A70 70 0 0 0 500 330Z" fill="#ec1a8c"/>
    <path d="M110 500 A140 140 0 0 0 255 620 L255 500Z" fill="#ec1a8c"/>
    <path d="M50 618 A46 46 0 0 1 142 618Z" fill="#f7a6cf"/>
  </svg>
  <div class="abs photo round" role="img" aria-label="Portrait of a smiling woman with glasses" style="left:711px;top:118px;width:132px;height:132px"></div>
  <div class="abs photo round" role="img" aria-label="Portrait of a businesswoman" style="left:554px;top:323px;width:176px;height:176px"></div>
  <div class="abs photo round" role="img" aria-label="Portrait of a man in glasses" style="left:1130px;top:400px;width:100px;height:130px"></div>
  <div class="abs photo round" role="img" aria-label="Two colleagues reviewing documents" style="left:954px;top:592px;width:152px;height:125px"></div>
  <div class="abs tablet"><div class="photo" role="img" aria-label="Support agent with a headset working at a laptop"></div></div>
  <div class="abs ghost-word">Brisk</div>
</section>

<section class="trust">
  <div class="abs trust-panel"></div>
  <h2 class="abs section-title trust-title">Why Companies Trust BRISK The Answer</h2>
  <div class="abs card" style="left:244px;top:915px;width:229px;height:263px">
    <svg width="62" height="62" viewBox="0 0 62 62" fill="none" stroke="#ec1a8c" stroke-width="2"><circle cx="44" cy="14" r="9"/><path d="M38 22l-6 10"/><rect x="30" y="36" width="12" height="20"/><rect x="44" y="30" width="12" height="26"/><circle cx="16" cy="14" r="6"/><path d="M8 56l4-20 8-6 6 8"/></svg>
    <h3>Market Leader</h3><p>We combine deep expertise with modern solutions to deliver reliable payroll services.</p></div>
  <div class="abs card" style="left:492px;top:915px;width:230px;height:263px">
    <svg width="62" height="62" viewBox="0 0 62 62" fill="none" stroke="#ec1a8c" stroke-width="2"><rect x="12" y="8" width="34" height="46" rx="3"/><rect x="22" y="4" width="14" height="8" rx="2"/><path d="M18 22h4M26 22h14M18 32h4M26 32h14M18 42h4M26 42h8"/><circle cx="46" cy="48" r="8"/><path d="M42 48l3 3 5-6"/></svg>
    <h3>Compliant</h3><p>Aligned with Swiss labor law, social contributions, and insurance obligations.</p></div>
  <div class="abs card" style="left:741px;top:915px;width:230px;height:263px">
    <svg width="62" height="62" viewBox="0 0 62 62" fill="none" stroke="#ec1a8c" stroke-width="2"><circle cx="31" cy="31" r="10"/><circle cx="31" cy="31" r="18" stroke-dasharray="6 4"/><path d="M8 42a26 26 0 0 0 46 0M54 20a26 26 0 0 0-46 0"/><circle cx="12" cy="48" r="4"/><circle cx="50" cy="14" r="4"/></svg>
    <h3>Agile &amp; Digital</h3><p>Fast, transparent, and 100% digital — tailored to your needs.</p></div>
</section>

<section class="payrolling">
  <div class="abs round" style="left:-150px;top:1430px;width:440px;height:440px;background:#fbd6e8"></div>
  <div class="abs round" style="left:588px;top:1290px;width:96px;height:96px;background:#e4e4e6"></div>
  <div class="abs photo pay-photo" role="img" aria-label="Two colleagues reviewing paperwork at a desk"></div>
  <h2 class="abs pay-title">What is Payrolling?</h2>
  <p class="abs pay-text">Payrolling is the simplest way to manage flexible employees. Instead of handling employment contracts, salaries, insurance, and compliance yourself, you entrust us with these tasks. Your workers remain available for you, while we take care of:</p>
  <ul class="abs bullets"><li>Employment contracts</li><li>Monthly payroll &amp; social contributions</li><li>Insurance &amp; benefits</li><li>Legal compliance</li></ul>
  <p class="abs tagline">You manage the people. We manage the paperwork.</p>
</section>

<section class="about">
  <div class="abs grey-band"></div>
  <p class="abs about-label">About &nbsp;Us</p>
  <h2 class="abs about-title">BRISK The Answer</h2>
  <p class="abs about-text">BRISK The Answer is part of the BRISK Group, alongside BRISK The+ Horizon and BRISK Your Stride. We bring expertise, trust, and innovation to workforce management.</p>
  <div class="abs photo round" role="img" aria-label="Two businesswomen working together on a laptop" style="left:606px;top:1868px;width:430px;height:430px"></div>
  <div class="abs play"><svg width="20" height="20" viewBox="0 0 20 20"><path d="M5 3l12 7-12 7z" fill="#fff"/></svg></div>
</section>

<section class="mission">
  <h2 class="abs section-title mission-title">Our mission is simple</h2>
  <div class="abs mcard" role="img" aria-label="Hand signing a document" style="left:187px"></div>
  <div class="abs mcard" role="img" aria-label="Colleagues reviewing documents in an office" style="left:469px"></div>
  <div class="abs mcard" role="img" aria-label="Team meeting around a table" style="left:751px"></div>
  <div class="abs mlabel" style="left:211px">To make employment administration hassle-free.</div>
  <div class="abs mlabel" style="left:493px">To ensure compliance with Swiss labor laws.</div>
  <div class="abs mlabel" style="left:775px">To help companies stay agile and responsive.</div>
</section>

<section class="testimonials">
  <h2 class="abs section-title test-title">What Our Clients Says</h2>
  <svg class="abs quote-ghost" width="140" height="100" viewBox="0 0 140 100"><path d="M0 100V55C0 20 18 4 50 0v22C34 26 28 36 28 50h22v50zM78 100V55C78 20 96 4 128 0v22c-16 4-22 14-22 28h22v50z" fill="#fbdcea"/></svg>
  <div class="abs quote-box"><svg width="96" height="96" viewBox="0 0 96 96"><path d="M26 66V50c0-12 6-18 18-20v8c-5 1-8 4-8 10h8v18zM52 66V50c0-12 6-18 18-20v8c-5 1-8 4-8 10h8v18z" fill="#fff"/></svg></div>
  <p class="abs quote-text">BRISK The Answer stands out for being agile and digital. Their platform is easy to use, communication is fast, and the entire process is transparent. We can count on them whenever we need quick answers and flexible solutions.</p>
  <div class="abs stars">★★★★★</div>
  <p class="abs author">Mark T., Freight Forwarder</p>
  <div class="abs dots"><i></i><i></i><i></i></div>
</section>

<footer>
  <svg class="abs footer-shape" width="1200" height="454" viewBox="0 0 1200 454">
    <path d="M0 120C300 0 800 -20 1200 150V454H0Z" fill="#f7c7e0"/>
    <path d="M0 130C320 20 760 20 1110 130 1150 145 1180 165 1200 185V454H0Z" fill="#333438"/>
  </svg>
  <div class="abs form-card">
    <h2>Get in touch</h2>
    <div class="field">Name</div><div class="field">Company</div><div class="field">Email Address</div><div class="field">Phone Number</div><div class="field area">How Can We Help You?</div>
  </div>
  <div class="abs btn send">Send</div>
  <h2 class="abs talk-title">Let’s Talk</h2>
  <p class="abs talk-text">Have questions about how payrolling works or want to know how we can support your company? Contact us today.</p>
  <div class="abs brand f-brand"><div class="brand-name">BRISK</div><div class="brand-tag">THE ANSWER</div></div>
  <div class="abs fcol" style="left:469px;top:3808px"><h4>Quick Links</h4><p>Home</p><p>What is Payrolling?</p><p>Who We Are</p><p>Contact</p></div>
  <div class="abs fcol" style="left:666px;top:3808px"><h4>Legal Links</h4><p>Privacy Policy</p><p>Terms &amp; Conditions</p><h4 style="margin-top:22px">Group Mention</h4><p>BRISK The Horizon</p><p>BRISK Your Stride</p></div>
  <div class="abs fcol" style="left:880px;top:3808px"><h4>Contact Us</h4><p><span class="ic">✆</span>+41 XX XXX XX XX</p><p><span class="ic">✉</span>info@brisktheanswer.example</p><p><span class="ic">⚲</span>BRISK The Answer<br><span style="padding-left:18px">[Street Address Placeholder]</span><br><span style="padding-left:18px">[ZIP, City, Switzerland]</span></p></div>
  <div class="abs f-rule"></div>
  <p class="abs copy">© 2025 BRISK THE ANSWER. ALL RIGHTS RESERVED.</p>
  <div class="abs to-top"><svg width="14" height="14" viewBox="0 0 14 14"><path d="M2 9l5-5 5 5" stroke="#fff" stroke-width="2" fill="none"/></svg></div>
</footer>
</body>
</html>
```